Commercial Construction Interior Fitout company needs Logo and Business Cards

We need a logo and business card design. We specialise in Commercial Ceilings, Partitions, Plastering and Carpentry.

Company name: 7QX Commercial Interiors. Would like a professional looking card more than a fancy look. Gloss front preferably black pattern with Fluro Green and white text.

Will need:

Name
Position
Phone
Fax
Email
Postal Address
Web address
Updates

Thank you so much everyone for your efforts and fantastic designs..   If I didn't respond to everyone personally,  my apologises. 

Again, thanks all

R.M                               

Target Market(s)

Existing & New clients in the Construction Industry

Industry/Entity Type

Business

Requirements
Nice to have
• 7QX to be overlapped or made into some sort of Logo

```html
<!DOCTYPE html>
<html lang="en">
<head>
<meta charset="utf-8">
<title>7QX Commercial Interiors – Business Card</title>
<link rel="stylesheet" href="https://fonts.googleapis.com/css2?family=Cinzel:wght@400&family=Source+Sans+3:wght@400;600&display=swap">
<style>
  :root {
    --page: #e7e4e0;
    --card: #0b0b0c;
    --card-edge: #151517;
    --band-a: #1c1d1f;
    --band-b: #2a2b2e;
    --green: #58c43c;
    --green-deep: #2e8f2a;
    --white: #f4f4f2;
  }
  * { margin: 0; padding: 0; box-sizing: border-box; }
  html, body { width: 1200px; height: 1200px; overflow: hidden; background: var(--page); }
  .stage { position: relative; width: 1200px; height: 1200px; }

  .card {
    position: absolute; left: 145px; width: 910px; height: 520px;
    background: linear-gradient(115deg, var(--card) 0%, var(--card) 62%, var(--card-edge) 63%, #111113 100%);
    border-radius: 26px; overflow: hidden;
    box-shadow: 0 14px 30px rgba(0,0,0,.25);
  }
  .card--front { top: 45px; }
  .card--back { top: 635px; }

  .texture-band {
    position: absolute; left: 0; right: 0; top: 150px; height: 200px;
    background: linear-gradient(90deg, var(--band-a) 0%, var(--band-b) 35%, rgba(30,31,33,.4) 70%, var(--band-b) 100%);
    opacity: .75;
  }
  .card--back .texture-band { top: 170px; height: 180px; }

  .brand {
    position: absolute; left: 0; right: 0; top: 200px;
    display: flex; align-items: center; justify-content: center; gap: 22px;
  }
  .brand-rule { height: 2px; width: 170px; background: linear-gradient(90deg, transparent, var(--green-deep)); }
  .brand-rule--right { background: linear-gradient(90deg, var(--green-deep), transparent); }
  .brand-mark { width: 22px; height: 22px; background: var(--green); }
  .brand-name {
    font-family: "Source Sans 3", sans-serif; font-weight: 600; font-size: 46px;
    color: var(--white); letter-spacing: 1px;
  }

  .contact {
    position: absolute; left: 90px; top: 150px; width: 360px;
    font-family: "Source Sans 3", sans-serif; font-size: 22px; line-height: 34px;
    color: var(--white); list-style: none;
  }
  .contact li { display: flex; justify-content: flex-end; align-items: center; gap: 16px; }
  .contact li span { text-align: right; }
  .contact .icon { width: 16px; height: 16px; flex: none; }
  .contact .address { align-items: flex-start; }
  .contact .address .icon { margin-top: 9px; }

  .divider {
    position: absolute; left: 490px; top: 60px; width: 2px; height: 380px;
    background: linear-gradient(180deg, transparent, var(--green) 50%, transparent);
  }
  .person { position: absolute; left: 540px; top: 215px; }
  .person-name { font-family: "Cinzel", serif; font-size: 34px; color: var(--white); letter-spacing: 1px; }
  .person-role { font-family: "Source Sans 3", sans-serif; font-size: 26px; color: var(--green); margin-top: 4px; }
</style>
</head>
<body>
<main class="stage">

  <section class="card card--front">
    <div class="texture-band" role="img" aria-label="Fine grey square dot pattern band"></div>
    <div class="brand">
      <span class="brand-rule"></span>
      <span class="brand-mark"></span>
      <span class="brand-name">7QX Commercial Interiors</span>
      <span class="brand-rule brand-rule--right"></span>
    </div>
  </section>

  <section class="card card--back">
    <div class="texture-band" role="img" aria-label="Fine grey square dot pattern band"></div>
    <ul class="contact">
      <li><span>1555 010 2200 000</span>
        <svg class="icon" viewBox="0 0 16 16"><path d="M4 1l3 3-2 2c1 2 3 4 5 5l2-2 3 3-2 2C7 14 2 9 2 3z" fill="var(--green)"/></svg></li>
      <li><span>1555 010 2200 012</span>
        <svg class="icon" viewBox="0 0 16 16"><rect x="4" y="1" width="8" height="5" fill="none" stroke="var(--green)" stroke-width="1.5"/><rect x="1" y="6" width="14" height="7" rx="1" fill="var(--green)"/></svg></li>
      <li><span>tomas@7qxcommercial.com</span>
        <svg class="icon" viewBox="0 0 16 16"><rect x="1" y="3" width="14" height="10" fill="none" stroke="var(--green)" stroke-width="1.5"/><path d="M1 3l7 6 7-6" fill="none" stroke="var(--green)" stroke-width="1.5"/></svg></li>
      <li><span>www.7qxcommercial.com</span>
        <svg class="icon" viewBox="0 0 16 16"><circle cx="8" cy="8" r="7" fill="none" stroke="var(--green)" stroke-width="1.5"/><path d="M1 8h14M8 1c-3 4-3 10 0 14M8 1c3 4 3 10 0 14" fill="none" stroke="var(--green)" stroke-width="1.2"/></svg></li>
      <li class="address"><span>Harlow House, Merton Plaza,<br>Merton Place, Dublin 4, Ireland</span>
        <svg class="icon" viewBox="0 0 16 16"><path d="M8 15C4 10 3 8 3 6a5 5 0 0110 0c0 2-1 4-5 9z" fill="var(--green)"/><circle cx="8" cy="6" r="2" fill="var(--card)"/></svg></li>
    </ul>
    <div class="divider"></div>
    <div class="person">
      <p class="person-name">Tomas Reilly</p>
      <p class="person-role">Director</p>
    </div>
  </section>

</main>
</body>
</html>
```